依頼詳細
第一回公演のチラシデザインを依頼したいです。

初回公演のタイトルは「日々硝子」

人は生きているだけで無数のドラマを生み出す。
それはその人に取っては重要で、他人にとっては些細な一面。
誰にもいうことはないけれど、自分の中で確かに起きる数々の感情の変化。
友情、恋愛、家族、夢。
何が人を作り、何が人を動かすのか。
誰かの長い人生のほんの一部を切り取り並べた『日々硝子』
あなたの中にもきっとある。
そんな感情のストーリー。

このようなテーマのダンス公演です。

■チラシのイメージは
<表面>
「水彩画」
「ステージで1本のスポットライトを浴びている女性」
「タイトル文字」

<裏面>
表面のイメージを採用しつつ、下記記載事項を掲載して下さい。

裏面→イベント名、日程、アクセス
チケット料金、問い合わせ先
出演者の名前、スタッフクレジット、SNSへのQRコード

デザインの雰囲気は暗めで、
記載項目
【フライヤーの記載内容詳細】
・記載事項
表面
イベントタイトル「日々硝子」

裏面

イベント名:Dance Company PEX第一回公演「日々硝子」

日程:2022年9月3日(土)・4日(日)

アクセス:会場「ヴェルナ・ホール」
https://verna-hall.example/access/

チケット料金:¥3,000

問い合わせ先:公式インスタグラムよりDM

出演:ぬい/朝比奈澄/宇野咲良/辻堂早苗/森永つばさ/浜口紗英/桑原理恵/堀ゆずは/綾瀬千尋/今井澪/葛西陽一郎/北条美奈子/戸部和泉/菅野拓真

スタッフクレジット
制作:矢島紬/根本彩花/江藤まどか
振付:菅野拓真/ぬい/朝比奈澄/宇野咲良/葛西陽一郎/北条美奈子
照明:株式会社ペルカ
音響:杉浦晃司

SNSへのQRコード→インスタグラムURLはこちら
https://www.instagram.com/dancecompanypex/?igshid=QxRtUwVb9Z=

主催:株式会社VEN
サイズ
A5
ページ数
両面
希望イメージ
シンプル 複雑
単色 カラフル
暗い 明るい
日常 高級
遊び心 厳粛
未来的 伝統的
女性的 男性的
希望する色
青系、無彩色系
納品ファイル
• 高解像度JPG (.jpg)
• イラストレーター形式 (.ai)
補足説明
※記載事項の詳細につきましては現状仮となっております。
※添付ファイルについて
フライヤー表面のイメージ画像を添付しておりますので、色味や質感、雰囲気を参考にしていただけたらと思います。
ご確認を宜しくお願い致します。
■ 選んだ理由

こちらのイメージをしっかりと組んだ水彩画でのデザインをご提案くださいました。

■ 提案者全員のお礼・コメント

この度はコンペにご参加頂きありがとうございました。
素敵なデザインをご提案くださり大変助かりました!!

```html
<!DOCTYPE html>
<html lang="ja">
<head>
<meta charset="UTF-8">
<title>日々硝子 | Dance Company PEX</title>
<link rel="stylesheet" href="https://fonts.googleapis.com/css2?family=Shippori+Mincho:wght@400;600&family=Cormorant+Garamond:wght@500&display=swap">
<style>
  :root {
    --frame: #5b5350;
    --stage-dark: #121113;
    --ink-white: #f3f1ee;
    --ink-warm: #e9d9a8;
    --accent-orange: #e58a2c;
    --muted: #d8d2cc;
  }
  * { margin: 0; padding: 0; box-sizing: border-box; }
  html, body { width: 848px; height: 1200px; overflow: hidden; }
  body {
    background: var(--frame);
    font-family: "Shippori Mincho", serif;
    color: var(--ink-white);
    position: relative;
  }
  .stage {
    position: absolute;
    left: 30px; top: 30px;
    width: 788px; height: 1028px;
    overflow: hidden;
    background: var(--stage-dark);
  }
  .stage-visual {
    position: absolute; inset: 0;
    background:
      radial-gradient(ellipse 38% 55% at 38% 38%, rgba(190,186,192,0.45) 0%, rgba(110,104,110,0.25) 45%, rgba(20,19,21,0) 100%),
      radial-gradient(ellipse 70% 70% at 42% 55%, #3a3639 0%, #201e21 55%, #0e0d0f 100%);
  }
  .tagline {
    position: absolute;
    left: 34px; top: 118px;
    font-size: 18px;
    line-height: 1.6;
    letter-spacing: 0.04em;
  }
  .tagline .warm { color: var(--ink-warm); }
  .title {
    position: absolute;
    right: 44px; top: 80px;
    writing-mode: vertical-rl;
    font-size: 114px;
    font-weight: 400;
    letter-spacing: 0.3em;
    line-height: 1;
    color: var(--ink-white);
  }
  .info-bar {
    position: absolute;
    left: 30px; right: 30px; bottom: 28px;
    height: 100px;
    display: flex;
    align-items: center;
  }
  .date {
    display: flex; align-items: center;
    color: var(--accent-orange);
    font-weight: 600;
  }
  .date-year {
    writing-mode: vertical-rl;
    font-size: 17px;
    letter-spacing: 0.05em;
    margin-right: 6px;
  }
  .date-days { font-size: 42px; letter-spacing: 0.01em; }
  .date-days small { font-size: 22px; }
  .venue {
    display: flex; align-items: center;
    margin-left: 30px;
    font-size: 17px;
    color: var(--muted);
  }
  .venue-mark {
    width: 26px; height: 26px;
    background: var(--muted);
    margin-right: 14px;
  }
  .company {
    margin-left: auto;
    font-family: "Cormorant Garamond", serif;
    font-size: 22px;
    color: var(--muted);
  }
</style>
</head>
<body>
  <main class="stage">
    <div class="stage-visual" role="img" aria-label="水彩画風の暗い舞台で一本のスポットライトを浴びて立つ女性の後ろ姿"></div>

    <p class="tagline">
      誰かの長い人生の<br>
      ほんの一部を切り取り並べた『日々硝子』<br>
      <span class="warm">あなたの中にもきっとある。<br>
      そんな感情のストーリー。</span>
    </p>

    <h1 class="title">日々硝子</h1>
  </main>

  <footer class="info-bar">
    <div class="date">
      <span class="date-year">2022</span>
      <span class="date-days">9.3<small>(土)</small>・9.4<small>(日)</small></span>
    </div>
    <div class="venue">
      <span class="venue-mark"></span>
      <span class="venue-name">ヴェルナ・ホール</span>
    </div>
    <div class="company">Dance Company PEX</div>
  </footer>
</body>
</html>
```